Vasel Tea Label & packaging for a premium tea brand. For local and global market

Create a look and feel for a box and rectangle tin. We are looking for a luxe packaging design for a new tea brand based in Kenya called 'Vasel Tea'. Kenya is home to the finest teas in the world and Vasel tea looks to embody that fact. Vasel Tea uses the most premium of Kenyan Tea, Black tea, Purple tea, White Tea, Green tea, Hibiscus Tea and Moringa Tea. Vasel Tea is handpicked from Kenya's highlands. This project will include the look and feel of the different teas described above. The copy on the main face of the box should read 'Premium Kenyan Tea' The box will contain 25 tagged tea bags, with a net weight of 50 gms.

On one side of the box will read 'packaging instructions' To fully savour this Vasel premium tea, use one tea bag for each cup, add some freshly bolded water and wait for 2 minutes as you enjoy the sweet aroma of our tea, stir and serve' Ingredients : Black Tea, and for the others the same : Hibiscus Tea, Green Tea, Purple Tea, White tea. should also feature on the label: Produce of Kenya.

Target Market(s)

Premium

Industry/Entity Type

Agribusiness

Font styles to use
Script

Colors

Designer to choose colors to be used in the design.

Requirements
Must have
• Luxe look and feel
Nice to have
• I have attached the Vasel tea logo and images of brands I'd lile the designer to be inspired by.
Should not have
• Green and yellow colours

```html
<!DOCTYPE html>
<html lang="en">
<head>
<meta charset="utf-8">
<title>Vasel Tea – Box Faces</title>
<link rel="stylesheet" href="https://fonts.googleapis.com/css2?family=Cinzel:wght@400&family=Cormorant+Garamond:wght@400;500&display=swap">
<style>
  :root {
    --page: #ffffff;
    --ink-dark: #1b1a1f;
    --mint: #78c29e;
    --mint-text: #6db58f;
    --olive: #9fab3a;
    --olive-text: #a3ad3e;
    --plum: #5c2f3c;
    --plum-text: #5f3340;
    --tag-bg: #ffffff;
    --tag-text: #4a3a33;
    --white-text: #ffffff;
  }
  * { margin: 0; padding: 0; box-sizing: border-box; }
  html, body { width: 1200px; height: 1000px; overflow: hidden; background: var(--page); }
  .canvas { position: relative; width: 1200px; height: 1000px; }

  .face {
    position: absolute;
    width: 313px; height: 313px;
    background: var(--panel);
    overflow: hidden;
  }
  .face__band {
    position: absolute; top: 0; bottom: 0; width: 24px;
    background: var(--accent);
  }
  .face__band--left { left: 0; }
  .face__band--right { right: 0; }
  .face__pattern {
    position: absolute; top: 0; bottom: 0; left: 24px; right: 24px;
    background: var(--panel);
  }
  .face__tab {
    position: absolute; top: 0; left: 152px; width: 10px; height: 44px;
    background: var(--tab);
  }
  .face__tag {
    position: absolute; top: 42px; left: 127px; width: 58px; height: 36px;
    background: var(--tag-bg);
    display: flex; align-items: center; justify-content: center;
  }
  .face__brand {
    font-family: "Cinzel", serif; font-weight: 400; font-size: 11px;
    letter-spacing: 0.5px; color: var(--tag-text);
  }
  .face__title {
    position: absolute; left: 0; right: 0; top: 126px; text-align: center;
    font-family: "Cinzel", serif; font-weight: 400; font-size: 31px; line-height: 1;
    color: var(--title);
  }
  .face__subtitle {
    position: absolute; left: 0; right: 0; top: 163px; text-align: center;
    font-family: "Cinzel", serif; font-weight: 400; font-size: 12.5px; letter-spacing: 0.3px;
    color: var(--title);
  }
  .face__net {
    position: absolute; right: 36px; bottom: 12px; text-align: left;
    font-family: "Cormorant Garamond", serif; font-weight: 500; font-size: 10.5px; line-height: 1.25;
    color: var(--title);
  }

  .face--black  { left: 444px; top: 150px; --panel: var(--ink-dark); --accent: var(--mint);  --tab: var(--mint);  --title: var(--mint-text); }
  .face--white  { left: 53px;  top: 670px; --panel: var(--mint);     --accent: var(--ink-dark); --tab: var(--ink-dark); --title: var(--white-text); }
  .face--green  { left: 443px; top: 670px; --panel: var(--ink-dark); --accent: var(--olive); --tab: var(--olive); --title: var(--olive-text); }
  .face--purple { left: 834px; top: 670px; --panel: var(--ink-dark); --accent: var(--plum);  --tab: var(--plum);  --title: var(--plum-text); }
</style>
</head>
<body>
<main class="canvas">

  <section class="face face--black">
    <div class="face__band face__band--left"></div>
    <div class="face__pattern" role="img" aria-label="Radial pattern of line-drawn tea leaves in dark grey"></div>
    <div class="face__band face__band--right"></div>
    <div class="face__tab"></div>
    <div class="face__tag"><span class="face__brand">Vasel</span></div>
    <h2 class="face__title">BLACK</h2>
    <p class="face__subtitle">PREMIUM KENYAN TEA</p>
    <p class="face__net">25 Bags<br>50 gms</p>
  </section>

  <section class="face face--white">
    <div class="face__band face__band--left"></div>
    <div class="face__pattern" role="img" aria-label="Radial pattern of white line-drawn tea leaves on mint"></div>
    <div class="face__band face__band--right"></div>
    <div class="face__tab"></div>
    <div class="face__tag"><span class="face__brand">Vasel</span></div>
    <h2 class="face__title">WHITE</h2>
    <p class="face__subtitle">PREMIUM KENYAN TEA</p>
  </section>

  <section class="face face--green">
    <div class="face__band face__band--left"></div>
    <div class="face__pattern" role="img" aria-label="Radial pattern of line-drawn tea leaves in dark grey"></div>
    <div class="face__band face__band--right"></div>
    <div class="face__tab"></div>
    <div class="face__tag"><span class="face__brand">Vasel</span></div>
    <h2 class="face__title">GREEN</h2>
    <p class="face__subtitle">PREMIUM KENYAN TEA</p>
    <p class="face__net">25 Bags<br>50 gms</p>
  </section>

  <section class="face face--purple">
    <div class="face__band face__band--left"></div>
    <div class="face__pattern" role="img" aria-label="Radial pattern of line-drawn tea leaves in dark grey"></div>
    <div class="face__band face__band--right"></div>
    <div class="face__tab"></div>
    <div class="face__tag"><span class="face__brand">Vasel</span></div>
    <h2 class="face__title">PURPLE</h2>
    <p class="face__subtitle">PREMIUM KENYAN TEA</p>
    <p class="face__net">25 Bags<br>50 gms</p>
  </section>

</main>
</body>
</html>
```